Exciting letterhead design for startup company

We need a A4 letterhead designing.

See attached file which contains the logo (on 3 different coloured backgrounds) and then the address and contact information. It also contains 4 colours that can be used.

Looking for an imaginative design. We are a young, fresh startup website design company so need a letterhead that reflects our industry.

Font styles to use
Sans Serif

```html
<!DOCTYPE html>
<html lang="en">
<head>
<meta charset="utf-8">
<title>SiteForge Letterhead</title>
<link href="https://fonts.googleapis.com/css2?family=Open+Sans:wght@400;600&display=swap" rel="stylesheet">
<style>
  :root {
    --ink: #1e1e1e;
    --brand-blue: #3b9fd6;
    --brand-yellow: #f2b731;
    --brand-green: #7ab648;
    --charcoal: #3d3f42;
    --paper: #ffffff;
  }
  html, body {
    margin: 0;
    padding: 0;
    overflow: hidden;
    background: var(--paper);
  }
  .letterhead {
    position: relative;
    width: 849px;
    height: 1200px;
    background: var(--paper);
    font-family: "Open Sans", Arial, sans-serif;
    color: var(--ink);
    overflow: hidden;
  }
  .brand-name {
    position: absolute;
    left: 48px;
    top: 46px;
    margin: 0;
    font-size: 54px;
    font-weight: 600;
    letter-spacing: -1.5px;
    color: var(--ink);
    line-height: 1;
  }
  .header-stripe {
    position: absolute;
    left: 345px;
    right: 0;
    height: 14px;
  }
  .header-stripe--yellow { top: 68px; background: var(--brand-yellow); }
  .header-stripe--green { top: 88px; background: var(--brand-green); }

  .legal-note {
    position: absolute;
    left: 48px;
    top: 1114px;
    margin: 0;
    font-size: 14px;
    line-height: 20px;
  }
  .contact {
    position: absolute;
    left: 358px;
    top: 1112px;
    font-size: 14px;
    line-height: 22px;
  }
  .contact-row {
    display: flex;
    align-items: center;
    gap: 8px;
  }
  .contact-item {
    display: inline-flex;
    align-items: center;
    gap: 8px;
    margin-right: 22px;
  }
  .contact-icon {
    width: 14px;
    height: 14px;
    fill: var(--brand-blue);
    flex: none;
  }
  .footer-band {
    position: absolute;
    bottom: 0;
    height: 22px;
  }
  .footer-band--blue { left: 0; width: 425px; background: var(--brand-blue); }
  .footer-band--charcoal { left: 425px; right: 0; background: var(--charcoal); }
</style>
</head>
<body>
<div class="letterhead">
  <header>
    <h1 class="brand-name">SiteForge</h1>
    <div class="header-stripe header-stripe--yellow"></div>
    <div class="header-stripe header-stripe--green"></div>
  </header>

  <footer>
    <p class="legal-note">Registered in England &amp; Wales.<br>Company No 09274158.</p>
    <div class="contact">
      <div class="contact-row">
        <span class="contact-item">
          <svg class="contact-icon" viewBox="0 0 16 16" aria-hidden="true"><path d="M1 6c0-2 3-4 7-4s7 2 7 4l-3 1-1-2H5L4 7 1 6zM3 8h10l1 5H2l1-5z"/></svg>
          0845 210 7731
        </span>
        <span class="contact-item">
          <svg class="contact-icon" viewBox="0 0 16 16" aria-hidden="true"><path d="M1 3h14v10H1z M1 3l7 6 7-6" fill="var(--brand-blue)"/><path d="M1 3l7 6 7-6" fill="none" stroke="#fff" stroke-width="1.4"/></svg>
          hello@siteforge.co.uk
        </span>
      </div>
      <div class="contact-row">
        <span class="contact-item">
          <svg class="contact-icon" viewBox="0 0 16 16" aria-hidden="true"><path d="M8 0a5.5 5.5 0 0 0-5.5 5.5C2.5 10 8 16 8 16s5.5-6 5.5-10.5A5.5 5.5 0 0 0 8 0zm0 8a2.5 2.5 0 1 1 0-5 2.5 2.5 0 0 1 0 5z"/></svg>
          SiteForge Limited, Suite 4, Harbour Court, Leeds LS1 4AB.
        </span>
      </div>
    </div>
    <div class="footer-band footer-band--blue"></div>
    <div class="footer-band footer-band--charcoal"></div>
  </footer>
</div>
</body>
</html>
```